Lorraine Whitcombe Resume 2025

🎨 Design Aesthetic
Overall Look: Sophisticated, clean, minimalist — less “corporate template,” more “editorial/luxury brand.” Think Interiors Quarterly meets Pemberly Global Estates.
Colors:
Base: Warm white or ivory background (instead of stark white, which can feel clinical).
Accents: Soft taupe, blush beige, muted rose-gold, warm gray. These lean feminine, elegant, and upscale without being distracting.
Avoid heavy blacks — use charcoal gray for text.
🔤 Typography
You’ll want fonts that are timeless, system-available (no downloading), and upscale. Pairing one serif with one sans-serif is a proven high-end combo.
Primary Serif (for Name + Section Headers):
Georgia (classic, built-in)
Times New Roman (if you want ultra-traditional, though a bit expected)
Palatino Linotype (a softer, elegant serif)
Secondary Sans-serif (for body text):
Helvetica Neue (clean, luxury feel)
Calibri (simple, highly readable, professional)
Arial Narrow (refined but modern)
✨ Recommended pairing: Name/Headings in Georgia Bold + Body in Helvetica Neue Light → refined, professional, easy to use in all your collateral.
📐 Layout & Structure
Header (Top Third):
Your name large, centered or left-aligned.
Subline with phone, email, location in smaller font, spaced out with dividers (e.g., |).
Neutral line or subtle accent bar under the header (warm gray or muted blush).
Section Layout:
Plenty of white space (breathe between sections, upscale feel).
Clear section headers (all caps serif font, spaced letters for luxury look).
Use subtle horizontal rules in a soft accent color instead of thick lines.
Accents:
Very subtle shading in soft beige or blush for section backgrounds (not blocks, just highlights).
Icons kept minimal — avoid anything too “clip-arty.”
🖼 Visual Mood Reference
Imagine:
A high-end boutique hotel brand sheet
Valdine packaging tones (ivory, taupe, gold accent) but dialed down to be subtle
Editorial spacing like in Lustre or Nido Home
🗂 Sections to Highlight (for your pivot)
Profile / Objective – Short 2–3 lines at the top making clear you are pivoting into luxury real estate, with transferable leadership skills.
Experience – KTR Studio (as Owner, not Managing Partner) with emphasis on entrepreneurship, strategy, client growth.
Board Membership – Whitcombe Foundation role (philanthropy adds prestige).
Certifications – Shows discipline and learning.
Education – Clean, simple.
“I want a resume design that feels refined and luxury-oriented, clean and sophisticated, with soft neutral feminine tones (ivory, blush beige, taupe, warm gray). Font pairing should be elegant but standard (e.g., Georgia for headings + Helvetica Neue for body) so I can reuse across collateral without downloading special fonts. Layout should have lots of white space, understated lines/dividers, and feel like something you’d expect from a luxury real estate or fashion brand.”

```html
<!DOCTYPE html>
<html lang="en">
<head>
<meta charset="utf-8">
<title>Lorraine Whitcombe — Resume 2025</title>
<link rel="stylesheet" href="https://fonts.googleapis.com/css2?family=Gelasio:wght@600;700&family=Inter:wght@400;600;700&display=swap">
<style>
:root{
  --backdrop:#6e5559;
  --ivory:#fcfbe8;
  --plum:#5b4a4d;
  --portrait:#5e4b4f;
  --taupe:#8a6a6e;
  --ink:#2c3643;
  --rule:#6f6a70;
  --dot:#a08c8f;
  --serif:"Gelasio",Georgia,serif;
  --sans:"Inter",Helvetica,Arial,sans-serif;
}
*{margin:0;padding:0;box-sizing:border-box}
html,body{width:960px;height:1200px;overflow:hidden;background:var(--backdrop)}
.page{position:absolute;left:16px;top:0;width:927px;height:1200px;background:var(--ivory);font-family:var(--sans);color:var(--ink)}
.abs{position:absolute}
.portrait{left:61px;top:0;width:361px;height:505px;background:linear-gradient(160deg,#6a5559 0%,var(--portrait) 60%,#56434a 100%)}
.name{left:56px;top:532px;font-family:var(--serif);font-weight:700;color:var(--plum);font-size:56px;line-height:62px;letter-spacing:-.3px}
.contact{left:58px;display:flex;align-items:center;gap:9px;font-size:25px;color:var(--ink);line-height:30px}
.contact svg{flex:none}
.phone{top:695px}
.email{top:737px}
.hr{height:1px;background:var(--rule)}
.section-title{font-family:var(--serif);font-weight:700;color:var(--plum);letter-spacing:2.6px;text-transform:uppercase}
.profile-title{left:58px;top:838px;font-size:26px;line-height:30px}
.profile-text{left:58px;width:342px;font-size:13.6px;line-height:16.4px;color:var(--ink)}
.profile-text strong{font-weight:700}
.divider{left:466px;top:56px;width:1px;height:1091px;background:var(--rule)}
.col{left:505px;width:374px}
.h-exp{top:51px;font-size:24px;line-height:28px}
.company{top:88px;font-size:23px;font-weight:700;color:var(--taupe);line-height:28px}
.role{top:130px;font-size:20px;font-weight:600;color:var(--taupe);line-height:24px}
.pill{position:absolute;border:1.3px solid #8c8285;border-radius:20px;display:flex;align-items:center;justify-content:center;font-size:14px;color:var(--ink);white-space:nowrap}
.pill b{font-weight:700;margin-right:4px}
.pill.lg{left:755px;width:124px;height:24px}
.pill.sm{left:836px;width:44px;height:16px;font-size:10px;font-weight:700}
.body{font-size:12px;line-height:14.6px;color:var(--ink)}
.subhead{font-size:20px;font-weight:600;color:var(--taupe);line-height:24px}
.timeline{position:absolute;left:511px;width:1px;background:#b9a9ab}
.bullet{position:absolute;left:530px;width:330px;font-size:12px;line-height:14.6px;color:var(--ink)}
.bullet::before{content:"";position:absolute;left:-22px;top:3px;width:8px;height:8px;border-radius:50%;background:var(--dot)}
.board-role{top:575px;width:240px;font-size:14.6px;line-height:18px;font-weight:700;color:var(--taupe)}
.cert{position:absolute;left:530px;width:300px;font-size:11.6px;line-height:12.4px;color:var(--ink)}
.cert::before{content:"";position:absolute;left:-22px;top:2px;width:8px;height:8px;border-radius:50%;background:var(--dot)}
.cert .t{color:var(--taupe)}
.school{top:1080px;font-size:20.5px;font-weight:700;color:var(--taupe);line-height:24px}
.degree{top:1106px;font-size:12px;line-height:14px}
.updated{top:1134px;font-size:11.5px;letter-spacing:2px;line-height:14px;color:var(--ink)}
.updated span{color:var(--taupe);font-weight:700}
</style>
</head>
<body>
<main class="page">
  <div class="abs portrait" role="img" aria-label="Portrait photo of Lorraine Whitcombe in a white blazer"></div>

  <h1 class="abs name">LORRAINE<br>WHITCOMBE</h1>

  <div class="abs contact phone">
    <svg width="22" height="22" viewBox="0 0 22 22" aria-hidden="true"><circle cx="11" cy="11" r="11" fill="var(--plum)"/><path d="M7.3 6.2c.5-.4 1.1-.3 1.4.2l1 1.6c.3.5.2 1-.2 1.4l-.6.5c.5 1.2 1.4 2.2 2.6 2.8l.5-.6c.4-.4 1-.5 1.4-.2l1.6 1c.5.3.6 1 .2 1.4l-.7.8c-.6.6-1.5.8-2.3.5-2.8-1-5-3.2-6-6-.3-.8-.1-1.7.5-2.3z" fill="var(--ivory)"/></svg>
    <span>(555) 014-2290</span>
  </div>
  <div class="abs contact email">
    <svg width="22" height="22" viewBox="0 0 22 22" aria-hidden="true"><circle cx="11" cy="11" r="11" fill="var(--plum)"/><rect x="5.5" y="7.3" width="11" height="7.6" rx="1" fill="none" stroke="var(--ivory)" stroke-width="1.2"/><path d="M5.8 7.7 11 11.8l5.2-4.1" fill="none" stroke="var(--ivory)" stroke-width="1.2"/></svg>
    <span>Lorraine@ktrstudio.com</span>
  </div>

  <div class="abs hr" style="left:58px;top:810px;width:334px"></div>
  <h2 class="abs section-title profile-title">Profile</h2>
  <p class="abs profile-text" style="top:881px">Lorraine Whitcombe is an industry-leading media strategist and entrepreneur with 15+ years of experience across multiple industries. As <strong>Owner of the award-winning EDWOSB-certified agency KTR Studio Inc.,</strong> she drives performance across multiple departments and acts as an internal strategic advisor. Her expertise spans government project management and corporate workflows, providing a rare combination of entrepreneurship, leadership, and marketing strategy.</p>
  <p class="abs profile-text" style="top:1046px">Lorraine is now pursuing a full-time career in <strong>real estate,</strong> bringing her skills in negotiation, business development, and client relations to the Miami luxury market.</p>
  <div class="abs hr" style="left:58px;top:1147px;width:334px"></div>

  <div class="abs divider"></div>

  <h2 class="abs col section-title h-exp">Experience</h2>
  <div class="abs col company">KTR Studio, Inc.</div>
  <div class="abs col role">Owner</div>
  <div class="pill lg" style="top:131px"><b>2007 –</b>Present</div>
  <p class="abs col body" style="top:162px">As a business owner in the media and marketing space, Lorraine brings innovative insight and marketing ideas, becoming an industry expert for every client. Her creativity, flexibility, transparency, and results-driven approach lend to long-term partnerships across all business verticals. By working closely with clients, her teams create powerful media and marketing campaigns that engage and inspire.</p>

  <div class="abs col subhead" style="top:266px">Key Accomplishments</div>
  <div class="timeline" style="top:308px;height:140px"></div>
  <p class="bullet" style="top:297px">Scaled KTR Studio Inc.’s client base both commercially and federally during the COVID-19 pandemic.</p>
  <p class="bullet" style="top:335px">Conceptualized and organized large-scale campaigns while leading KTR to immense success despite market disruptions.</p>
  <p class="bullet" style="top:393px">Directed State Guard Reserve campaigns across 13+ states in the past 12 months.</p>
  <p class="bullet" style="top:436px">For the Northern State Guard, overhauled marketing efforts to be data-driven and high-performing, delivering 3M+ impressions, 700+ conversions (2.58% conversion rate), and a 533% decreased CPA (from $901 to $48 at launch).</p>

  <h2 class="abs col section-title" style="top:537px;font-size:24px;line-height:28px">Board Membership</h2>
  <div class="abs col board-role" style="left:505px">Active Board Member, The Eleanor Whitcombe &amp; Harold J. Whitcombe Memorial Foundation (The Whitcombe Foundation)</div>
  <div class="pill lg" style="top:576px"><b>2018 –</b>Present</div>
  <div class="timeline" style="top:673px;height:102px"></div>
  <p class="bullet" style="top:662px">Support governance, fundraising, and philanthropic initiatives dedicated to advancing music education and instrument preservation.</p>
  <p class="bullet" style="top:720px;width:340px">Collaborate with fellow board members to ensure compliance, organizational growth, and mission alignment.</p>
  <p class="bullet" style="top:764px">Represent family legacy and oversee strategic initiatives benefiting communities nationwide.</p>

  <h2 class="abs col section-title" style="top:819px;font-size:24px;line-height:28px">Certifications</h2>
  <div class="timeline" style="top:868px;height:158px"></div>
  <p class="cert" style="top:858px"><span class="t">Leadership for Sales and Marketing Professionals</span><br>Halvern Learning Group, Inc.</p>
  <div class="pill sm" style="top:859px">2018</div>
  <p class="cert" style="top:895px"><span class="t">Scaling Excellence Across the Organization</span><br>Halvern Learning Group, Inc.</p>
  <div class="pill sm" style="top:897px">2019</div>
  <p class="cert" style="top:931px"><span class="t">Northlane Email Marketing Certification</span></p>
  <div class="pill sm" style="top:930px">2019</div>
  <p class="cert" style="top:955px"><span class="t">Northlane Inbound Marketing Certification</span></p>
  <div class="pill sm" style="top:953px">2019</div>
  <p class="cert" style="top:979px"><span class="t">Executive Playbook:</span> Managing the 3 C’s,<br>Change, Conflict, and Communications – Halvern</p>
  <div class="pill sm" style="top:986px">2019</div>
  <p class="cert" style="top:1016px"><span class="t">21st Century Leadership</span> – Halvern Learning Group, Inc.</p>
  <div class="pill sm" style="top:1012px">2020</div>

  <h2 class="abs col section-title" style="top:1050px;font-size:24px;line-height:28px">Education</h2>
  <div class="abs col school">Lakeshore University</div>
  <div class="abs col body degree">Bachelor of Arts, Sociology</div>
  <div class="pill lg" style="top:1100px"><b>1993 – 1998</b></div>
  <div class="abs col updated"><span>Updated:</span> September 8, 2025</div>
</main>
</body>
</html>
```